Cultural Values, and Purpose, Vision and Mission statements design

We have recently created Cultural Values, and Purpose, Vision and Mission statements for a client’s business. We would like a visual representation created of each of these, to be hung on display in their office. For this project, we would like four (4) graphic design prints drawn up that depict:1. Purpose2. Vision3. Mission4. Cultural ValuesAll print designs should use a recurring, common theme, and be reflective of the business’ colours (see attached logo.)Please read and follow specifications in attached design brief.
Updates

Need extra days to review

Target Market(s)

Females, aged between 37 and 57 years old, who are family orientated, living locally, married and have between 1 and 3 children living at home.

Requirements
Must have
• Photoshop (PSD) format: All completed design will need to be in Photoshop (PSD) format before being handed over. This is to ensure that we can make alterations before printing if necessary.
• Quality: All designs must be 300 pixels resolution or higher.
• Purpose, Vision & Mission Designs Dimensions: The dimensions for each of the Purpose, Vision and Mission designs will need to be 30.5cm x 40.6cm (portrait, rectangle shape) with a surrounding 3.8cm border as it will be printed onto canvas matching these specifications.
• Cultural Values Dimensions: There are no specific dimensions required for the Cultural Values so the designer should feel free to display them best they see fit.
• Theme: All must follow the same theme and be reflective of the business's colours and logo.

```html
<!DOCTYPE html>
<html lang="en">
<head>
<meta charset="utf-8">
<title>KestrelAuto Vision and Mission Prints</title>
<link rel="stylesheet" href="https://fonts.googleapis.com/css2?family=Lato:wght@400;700&display=swap">
<style>
  :root {
    --orange: #f08323;
    --grey: #9b9c9e;
    --text-grey: #8a8b8d;
    --paper: #ffffff;
    --backdrop: #efe6de;
  }
  * { margin: 0; padding: 0; box-sizing: border-box; }
  html, body {
    width: 1200px;
    height: 874px;
    overflow: hidden;
    background: var(--backdrop);
    font-family: "Lato", sans-serif;
  }
  .print {
    position: absolute;
    top: 170px;
    width: 360px;
    height: 480px;
    background: var(--paper);
    overflow: hidden;
  }
  .print--vision { left: 152px; }
  .print--mission { left: 711px; }
  .corner-shapes {
    position: absolute;
    left: 0;
    top: 0;
    width: 360px;
    height: 480px;
  }
  .brand {
    position: absolute;
    left: 18px;
    top: 20px;
    display: flex;
    align-items: center;
    gap: 10px;
  }
  .brand__mark {
    width: 22px;
    height: 22px;
    background: var(--grey);
  }
  .brand__name {
    font-weight: 700;
    font-size: 26px;
    color: var(--orange);
    letter-spacing: -0.3px;
  }
  .heading {
    position: absolute;
    left: 18px;
    top: 96px;
    display: flex;
    align-items: center;
    gap: 9px;
  }
  .heading__icon { width: 45px; height: 42px; }
  .heading__title {
    font-weight: 700;
    font-size: 30px;
    color: var(--orange);
    letter-spacing: 0.3px;
  }
  .statement {
    position: absolute;
    left: 21px;
    border-left: 5px solid var(--orange);
    padding-left: 12px;
    font-size: 13.6px;
    line-height: 17.6px;
    color: var(--text-grey);
  }
  .print--vision .statement { top: 156px; }
  .print--mission .statement { top: 150px; }
  .statement__line {
    display: block;
    white-space: nowrap;
  }
  .statement__line--justified {
    text-align: justify;
    text-align-last: justify;
    white-space: normal;
  }
</style>
</head>
<body>

<section class="print print--vision">
  <svg class="corner-shapes" viewBox="0 0 360 480" aria-hidden="true">
    <polygon points="360,198 360,480 110,480" fill="var(--orange)"/>
    <polygon points="0,480 0,450 60,480" fill="var(--grey)"/>
  </svg>
  <div class="brand">
    <span class="brand__mark"></span>
    <span class="brand__name">KestrelAuto</span>
  </div>
  <div class="heading">
    <svg class="heading__icon" viewBox="0 0 45 42" aria-hidden="true">
      <path d="M2 21 Q22.5 5 43 21 Q22.5 37 2 21 Z" fill="none" stroke="var(--grey)" stroke-width="3"/>
      <circle cx="22.5" cy="21" r="7" fill="var(--grey)"/>
    </svg>
    <h2 class="heading__title">VISION</h2>
  </div>
  <p class="statement">
    <span class="statement__line statement__line--justified" style="width:296px">We will earn our reputation for being the</span>
    <span class="statement__line statement__line--justified" style="width:272px">number one, family focused, automotive</span>
    <span class="statement__line statement__line--justified" style="width:248px">specialists throughout the Latrobe</span>
    <span class="statement__line">Valley.</span>
  </p>
</section>

<section class="print print--mission">
  <svg class="corner-shapes" viewBox="0 0 360 480" aria-hidden="true">
    <polygon points="360,198 360,480 110,480" fill="var(--orange)"/>
    <polygon points="0,480 0,450 60,480" fill="var(--grey)"/>
  </svg>
  <div class="brand">
    <span class="brand__mark"></span>
    <span class="brand__name">KestrelAuto</span>
  </div>
  <div class="heading">
    <svg class="heading__icon" viewBox="0 0 45 42" aria-hidden="true">
      <line x1="8" y1="4" x2="8" y2="30" stroke="var(--orange)" stroke-width="3"/>
      <polygon points="9,4 30,4 25,10 30,16 9,16" fill="var(--orange)"/>
      <polyline points="2,40 12,26 20,34 30,22 43,40" fill="none" stroke="var(--grey)" stroke-width="2"/>
    </svg>
    <h2 class="heading__title">MISSION</h2>
  </div>
  <p class="statement">
    <span class="statement__line statement__line--justified" style="width:310px">Through the delivery of high-quality automotive</span>
    <span class="statement__line statement__line--justified" style="width:288px">services and customer experience</span>
    <span class="statement__line">excellence, we will instil confidence and</span>
    <span class="statement__line">security into our clients. We will build</span>
    <span class="statement__line">a solid platform of trust in which</span>
    <span class="statement__line statement__line--justified" style="width:194px">our entire industry will</span>
    <span class="statement__line">recognise the benefits</span>
  </p>
</section>

</body>
</html>
```